2023 Wall Calendar Design - 11" x 8.5"

OVERVIEW:

The theme for this calendar is American (red-white-blue) and should have a modern feel. Please see website links and attached logos.

This calendar will feature screenshots and behind-the-scenes photos from all Harbor Lantern Shows found on our website.

We will supply screenshots for you to choose from via a Dropbox link once selected. Some sample screenshots are attached to get you started on design concepts.

SPECIFICATIONS:

28 PAGES – Cover, Back Cover, Inside Cover x 2, 24 calendar pages @ 2 pages / month

SIZE: 11” x 8.5” finished – excluding bleed

FULL COLOR – CMYK

See deliverables at bottom also.

DESIGN & THEME:

Each page will be 11" x 8.5" finished (excluding bleed margins) and have 2 pages for each month plus front and back cover and inside pages - total 28 pages. A sizing template is attached for your reference.

The pages will have a scoring hole for hanging on the wall.

The front cover will be a cover design that should make the calendar look appealing and reflect our brand and theme well.

Please see our websites listed below to get a feel for our branding.

INSIDE DESIGN INFO:

For the calendar date pages there will be a main photo on 1 page with a short photo description. On the dates page, the dates will be in squares so a person can write in them (IMPORTANT).

Relevant squares will also have special days in them including show premiere dates, US holidays, show stars birthdays, company anniversary, etc.

Some date pages may / can have mini photos on them as well. Some months have more than 1 photo that could be used if the design works for it.

We will supply special dates & holidays shortly but want to get started on the design style now while we complete assembly of the dates.

The inside cover pages (2) will have some info about our brand and maybe some photos that didn't make it into the main calendar pages.

The back cover can have a collage of all 12 main photos like they normally have with wall calendars that you buy on sites like Pagefold.example.

SOME CALENDAR LAYOUTS WE LIKE:
Not necessarily the STYLE/DESIGN but the LAYOUT for content only:

https://www.pagefold.example/shop/item-a-2023-wall-calendar/100000000001

https://www.pagefold.example/shop/item-b-2023-wall-calendar/100000000002

https://www.pagefold.example/shop/item-c-2023-wall-calendar/100000000003

https://www.pagefold.example/shop/item-d-2023-wall-calendar/100000000004

https://www.pagefold.example/shop/item-e-2023-wall-calendar/100000000005

https://www.pagefold.example/shop/item-f-2023-wall-calendar/100000000006

NOTE: I've also attached a mock-up of our 2022 calendar so you can see it.

DESIGN COLLATERAL:

We've attached our corporate logos, fonts, and some sample images that can be used in the calendar to start the layout concepts.

We will be compiling special dates and featured text while we review design concepts to select our winner.

Logo font - Stencil - https://typeshelf.example/fonts/stencil

Company sites: HarborLanternMedia.example | HarborLantern.example

Deliverables:

Full CMYK color, print ready PDF file formatted to 350 dpi – max file size 75 MB

Use attached template to finalize file sizes & bleeds

Fully editable layered AI source file (DO NOT USE COREL DRAW – we cannot read these files)

Fully editable In Design source file

Fully editable layered PSD source file (smart objects preferred)

Supply all fonts used so we may edit the calendar later – fonts must be licensed for your commercial use already or contact us to acquire any needed fonts.

We have licenses for all Adobe & Envato Elements fonts. Google & Microsoft fonts are also options. If you need us to acquire fonts from Envato or Adobe for your use, please let us know.

We have the Adobe Creative Suite. Any files you supply must be compatible with this software for both reading AND editing – including text.

If you have any questions, please feel free to message us and ask them.

Thank you & good luck!

Target Market(s)

American entertainment fans of TV

Industry/Entity Type

Television

Colors
0054AA
0677BA
7BADD7
CADEEF
E8F1F8
EB3D1F
EC4F4E
F09395
F8D3D4
FCEDEE

Requirements
Must have
• calendar as specified with writable date squares - see brief

```html
<!DOCTYPE html>
<html lang="en">
<head>
<meta charset="utf-8">
<title>Harbor Lantern Shows – 2023 Wall Calendar</title>
<link rel="stylesheet" href="https://fonts.googleapis.com/css2?family=Montserrat:ital,wght@0,500;0,600;0,700;0,800;1,800&display=swap">
<style>
  :root{
    --navy:#17346e;
    --blue:#0054AA;
    --red:#d62c2c;
    --red-bright:#EB3D1F;
    --panel:#e3e3e3;
    --line:#1f3a78;
    --paper:#ffffff;
    --stage:#efece8;
    --ink:#1b2b55;
  }
  *{box-sizing:border-box;margin:0;padding:0}
  html,body{width:1200px;height:900px;overflow:hidden}
  body{background:var(--stage);font-family:"Montserrat",sans-serif;color:var(--ink);position:relative}

  /* ---------- Front cover ---------- */
  .cover{position:absolute;left:30px;top:234px;width:560px;height:432px;background:var(--paper);overflow:hidden;box-shadow:0 4px 14px rgba(0,0,0,.18)}
  .cover-photo{position:absolute;inset:0;background:radial-gradient(circle at 55% 70%,#e0672a 0,#7a3a3a 18%,transparent 38%),linear-gradient(160deg,#2c3a66 0%,#3d4f86 45%,#262a40 100%)}
  .art{position:absolute;inset:0;width:100%;height:100%}

  /* ---------- Logo (text only) ---------- */
  .brand{position:absolute;display:flex;align-items:center;gap:8px}
  .brand-dot{width:14px;height:14px;border-radius:50%;background:var(--red)}
  .brand-name{font-weight:800;color:var(--navy);text-transform:uppercase;line-height:1.05}
  .brand-url{position:absolute;font-weight:700;color:var(--navy)}

  /* ---------- January page ---------- */
  .wall-page{position:absolute;left:620px;top:20px;width:550px;height:860px;background:var(--paper);overflow:hidden;box-shadow:0 4px 14px rgba(0,0,0,.18)}
  .month-photo{position:absolute;left:0;top:0;width:550px;height:430px;background:linear-gradient(180deg,#d9dbd6 0%,#c9ccc6 30%,#55724a 42%,#6c6f86 55%,#9a3a32 72%,#6b5a52 100%)}

  .month-tab{position:absolute;left:0;top:457px;width:122px;height:20px;background:var(--red);color:#fff;font-weight:700;font-size:13px;letter-spacing:.5px;padding-left:44px;line-height:20px;clip-path:polygon(0 0,100% 0,94% 100%,0 100%)}

  .grid{position:absolute;left:64px;top:476px;width:422px;display:grid;grid-template-columns:repeat(7,1fr);grid-template-rows:12px repeat(6,50.3px)}
  .day-head{font-size:6.4px;font-weight:700;color:#fff;text-align:center;line-height:12px;background:var(--navy);margin-right:4px;clip-path:polygon(6% 0,100% 0,94% 100%,0 100%)}
  .day-head.sun{background:var(--red);clip-path:none;margin-right:0}
  .cell{position:relative;border-right:1px solid var(--line);border-bottom:1px solid var(--line);background:#fff}
  .cell:nth-child(7n+1){border-left:1px solid var(--line)}
  .grid .cell.row1{border-top:1px solid var(--line)}
  .cell.sun{color:#fff;background:transparent}
  .date{position:absolute;right:4px;top:3px;font-size:11.5px;font-weight:600;color:var(--navy)}
  .cell.sun .date{color:#fff}
  .note{position:absolute;left:5px;bottom:4px;font-size:3.8px;font-weight:600;line-height:1.35;color:var(--navy)}
  .cell.sun .note{color:#fff}
  .sun-col{position:absolute;left:64px;top:488px;width:60.3px;height:302px;background:linear-gradient(180deg,#c42a35 0%,#8a2b4c 40%,#3a3468 70%,var(--navy) 100%)}

  .footer-year{position:absolute;left:127px;top:818px;font-size:19px;font-weight:800;font-style:italic;color:#fff;letter-spacing:1px}
</style>
</head>
<body>

<!-- FRONT COVER -->
<section class="cover" aria-label="Front cover">
  <div class="cover-photo" role="img" aria-label="Photo: friends gathered around a campfire at dusk with a guitar"></div>
  <svg class="art" viewBox="0 0 560 432" aria-hidden="true">
    <defs>
      <linearGradient id="bandCover" x1="0" y1="0" x2="0" y2="1">
        <stop offset="0" stop-color="#17346e"/><stop offset=".55" stop-color="#8a2b4c"/><stop offset="1" stop-color="#d62c2c"/>
      </linearGradient>
    </defs>
    <polygon points="522,0 560,0 560,432 300,432 340,345 420,345" fill="#fff"/>
    <polygon points="548,30 560,30 560,245 438,292" fill="url(#bandCover)"/>
    <g transform="translate(505,238)">
      <path d="M-34,-20 A40,40 0 0 1 30,-26" fill="none" stroke="#17346e" stroke-width="3"/>
      <path d="M34,20 A40,40 0 0 1 -30,26" fill="none" stroke="#d62c2c" stroke-width="3"/>
      <g transform="rotate(-30)" fill="#fff" font-family="Montserrat,sans-serif" font-weight="800" text-anchor="middle">
        <text y="-8" font-size="9">CALANDER</text>
        <text y="14" font-size="22" font-style="italic">2023</text>
      </g>
    </g>
    <g fill="#17346e">
      <circle cx="446" cy="312" r="1.6"/><circle cx="460" cy="322" r="1.6"/><circle cx="474" cy="318" r="1.6"/><circle cx="488" cy="310" r="1.6"/><circle cx="452" cy="334" r="1.6"/>
    </g>
  </svg>
  <div class="brand" style="left:360px;top:358px">
    <span class="brand-dot"></span>
    <span class="brand-name" style="font-size:17px">Harbor Lantern<br>Shows</span>
  </div>
  <span class="brand-url" style="left:420px;top:402px;font-size:8px">HarborLantern.example</span>
</section>

<!-- JANUARY PAGE -->
<section class="wall-page" aria-label="January calendar page">
  <div class="month-photo" role="img" aria-label="Photo: tractor pull at a county fair with black exhaust smoke and a crowd in the stands"></div>
  <svg class="art" viewBox="0 0 550 860" aria-hidden="true">
    <defs>
      <linearGradient id="bandPage" x1="0" y1="0" x2="0" y2="1">
        <stop offset="0" stop-color="#17346e"/><stop offset=".55" stop-color="#8a2b4c"/><stop offset="1" stop-color="#d62c2c"/>
      </linearGradient>
      <linearGradient id="footerBand" x1="0" y1="0" x2="1" y2="0">
        <stop offset="0" stop-color="#17346e"/><stop offset=".55" stop-color="#3a3468"/><stop offset="1" stop-color="#d62c2c"/>
      </linearGradient>
    </defs>
    <polygon points="530,0 550,0 550,430 303,430 345,348 470,348" fill="#fff"/>
    <polygon points="538,40 550,40 550,250 440,292" fill="url(#bandPage)"/>
    <g transform="translate(500,242)">
      <path d="M-34,-20 A40,40 0 0 1 30,-26" fill="none" stroke="#17346e" stroke-width="3"/>
      <path d="M34,20 A40,40 0 0 1 -30,26" fill="none" stroke="#d62c2c" stroke-width="3"/>
      <g transform="rotate(-30)" fill="#fff" font-family="Montserrat,sans-serif" font-weight="800" text-anchor="middle">
        <text y="-8" font-size="9">CALANDER</text>
        <text y="14" font-size="22" font-style="italic">2023</text>
      </g>
    </g>
    <g fill="#17346e">
      <circle cx="486" cy="304" r="1.6"/><circle cx="498" cy="314" r="1.6"/><circle cx="510" cy="310" r="1.6"/><circle cx="522" cy="302" r="1.6"/><circle cx="490" cy="326" r="1.6"/>
    </g>
    <!-- grey backing panel -->
    <polygon points="8,440 376,440 392,470 486,470 486,690 530,800 8,800" fill="#e3e3e3"/>
    <polyline points="8,800 8,440 376,440" fill="none" stroke="#fff" stroke-width="1"/>
    <circle cx="275" cy="445" r="4" fill="#fff"/>
    <!-- footer -->
    <polygon points="0,806 550,806 550,860 0,860" fill="url(#footerBand)"/>
    <polygon points="0,806 195,806 208,826 0,826" fill="#17346e"/>
    <rect x="8" y="812" width="534" height="41" fill="none" stroke="#fff" stroke-width=".8"/>
    <rect x="380" y="794" width="170" height="4" fill="#d62c2c"/>
    <rect x="450" y="800" width="100" height="2" fill="#d62c2c"/>
    <circle cx="275" cy="834" r="4" fill="#fff"/>
  </svg>

  <div class="brand" style="left:352px;top:360px">
    <span class="brand-dot"></span>
    <span class="brand-name" style="font-size:17px">Harbor Lantern<br>Shows</span>
  </div>
  <span class="brand-url" style="left:410px;top:404px;font-size:8px">HarborLantern.example</span>

  <div class="month-tab">JANUARY</div>
  <div class="sun-col" aria-hidden="true"></div>

  <div class="grid">
    <div class="day-head sun">SUNDAY</div><div class="day-head">MONDAY</div><div class="day-head">TUESDAY</div><div class="day-head">WEDNESDAY</div><div class="day-head">THURSDAY</div><div class="day-head">FRIDAY</div><div class="day-head">SATURDAY</div>

    <div class="cell sun row1"><span class="note">Note space here</span></div>
    <div class="cell row1"><span class="note">Short note here<br>Short note here<br>Short note here<br>Short note here<br>Short note here</span></div>
    <div class="cell row1"><span class="note">Short note here</span></div>
    <div class="cell row1"></div><div class="cell row1"></div><div class="cell row1"></div>
    <div class="cell row1"><span class="date">1</span></div>

    <div class="cell sun"><span class="date">2</span></div><div class="cell"><span class="date">3</span></div><div class="cell"><span class="date">4</span></div><div class="cell"><span class="date">5</span></div><div class="cell"><span class="date">6</span></div><div class="cell"><span class="date">7</span></div><div class="cell"><span class="date">8</span></div>

    <div class="cell sun"><span class="date">9</span></div><div class="cell"><span class="date">10</span></div><div class="cell"><span class="date">11</span></div><div class="cell"><span class="date">12</span></div><div class="cell"><span class="date">13</span></div><div class="cell"><span class="date">14</span></div><div class="cell"><span class="date">15</span></div>

    <div class="cell sun"><span class="date">16</span></div><div class="cell"><span class="date">17</span></div><div class="cell"><span class="date">18</span></div><div class="cell"><span class="date">19</span></div><div class="cell"><span class="date">20</span></div><div class="cell"><span class="date">21</span></div><div class="cell"><span class="date">22</span></div>

    <div class="cell sun"><span class="date">23</span></div><div class="cell"><span class="date">24</span></div><div class="cell"><span class="date">25</span></div><div class="cell"><span class="date">26</span></div><div class="cell"><span class="date">27</span></div><div class="cell"><span class="date">28</span></div><div class="cell"><span class="date">29</span></div>

    <div class="cell sun"><span class="date">30</span><span class="note">Short note here</span></div>
    <div class="cell"><span class="date">31</span></div>
    <div class="cell"></div>
    <div class="cell"><span class="note">Short note here<br>Short note here<br>Short note here</span></div>
    <div class="cell"></div><div class="cell"></div><div class="cell"></div>
  </div>

  <div class="brand" style="left:22px;top:812px;gap:5px">
    <span class="brand-dot" style="width:8px;height:8px;background:#fff"></span>
    <span class="brand-name" style="font-size:8.5px;color:#fff">Harbor Lantern<br>Shows</span>
  </div>
  <span class="footer-year">2023</span>
</section>

</body>
</html>
```